Chairside Roots: the dental helper's field guide, start to finish

Book cover:

Book about dental implantology
Reader is a dental assistant
Introduction to surgical knowledge to case acceptance. We will start with the intro to implants that will cover population stats on tooth loss, how to make the patient trust the team, how to communicate with the patient. Then we will get more technical; bone loss, bone quality and quantity. We will also inform on pros and cons of different classic dental treatments vs implant treatment. Surgical knowledge deep into various aspects of implants procedures. An illustration of surgical instruments needed and motors and hand pieces. Operatory set up will be demonstrated. I’ll be guiding the role of the surgical assistant and non surgical assistant. At the end I’ll explain how to close an implant case. From single implants to more complex cases.

Target Market(s)

Dental assistants

Industry/Entity Type

Dental

Font styles to use
Other font styles liked:
• Mellifluous or addington

Colors
EE7325
F08F49
F5BC92
FAE3D3
FDF4ED

Requirements
Must have
• Dental implant, positive vibe, orange Colors, professional
Nice to have
• Sense of team spirit, uncluttered,
Should not have
• Images of people

```html
<!DOCTYPE html>
<html lang="en">
<head>
<meta charset="utf-8">
<title>Chairside Roots – Book Cover</title>
<link rel="stylesheet" href="https://fonts.googleapis.com/css2?family=Newsreader:ital,opsz,wght@0,6..72,400;0,6..72,600;1,6..72,400&family=Gochi+Hand&display=swap">
<style>
  :root {
    --page-bg: #ffffff;
    --cover-blue: #0433ff;
    --grid-blue: #1a46ff;
    --implant-blue: #3a5fff;
    --title-orange: #f65a1f;
    --cream: #f5e6da;
    --line-white: #ffffff;
  }
  * { margin: 0; padding: 0; box-sizing: border-box; }
  html, body {
    width: 1200px;
    height: 1000px;
    overflow: hidden;
    background: var(--page-bg);
  }
  .canvas {
    position: relative;
    width: 1200px;
    height: 1000px;
  }
  .book-cover {
    position: absolute;
    left: 374px;
    top: 203px;
    width: 421px;
    height: 595px;
    background: var(--cover-blue);
    font-family: "Newsreader", Georgia, serif;
    color: var(--cream);
    overflow: hidden;
  }
  .blueprint-field {
    position: absolute;
    left: 29px;
    top: 211px;
    width: 369px;
    height: 368px;
    background: linear-gradient(180deg, var(--cover-blue) 0%, var(--grid-blue) 50%, var(--cover-blue) 100%);
  }
  .implant-art {
    position: absolute;
    left: 102px;
    top: 306px;
    width: 131px;
    height: 225px;
    background: var(--implant-blue);
    border-radius: 4px 4px 30px 30px;
  }
  .cover-title {
    position: absolute;
    top: 60px;
    left: 0;
    width: 100%;
    text-align: center;
    color: var(--title-orange);
    font-weight: 600;
    font-size: 48px;
    line-height: 38px;
    letter-spacing: -0.5px;
  }
  .tagline-row {
    position: absolute;
    top: 142px;
    left: 74px;
    width: 269px;
    display: flex;
    align-items: center;
    gap: 6px;
  }
  .tagline-rule {
    flex: 1;
    height: 1px;
    background: var(--cream);
  }
  .tagline {
    font-style: italic;
    font-size: 21px;
    line-height: 26px;
    white-space: nowrap;
  }
  .subtitle {
    position: absolute;
    top: 169px;
    left: 0;
    width: 100%;
    text-align: center;
    font-size: 17px;
    line-height: 22px;
  }
  .author-name {
    position: absolute;
    top: 210px;
    left: 0;
    width: 100%;
    text-align: center;
    font-size: 13.5px;
    line-height: 18px;
  }
  .callout-lines {
    position: absolute;
    left: 0;
    top: 0;
    width: 421px;
    height: 595px;
  }
  .callout {
    position: absolute;
    font-family: "Gochi Hand", "Comic Sans MS", cursive;
    font-size: 12px;
    line-height: 14px;
    color: var(--line-white);
    white-space: nowrap;
  }
  .callout--efficiency { left: 268px; top: 281px; }
  .callout--matters    { left: 270px; top: 364px; }
  .callout--takes      { left: 277px; top: 421px; }
  .callout--team       { left: 233px; top: 489px; }
</style>
</head>
<body>
<main class="canvas">
  <section class="book-cover">
    <div class="blueprint-field" role="img" aria-label="Faint blueprint grid background"></div>
    <div class="implant-art" role="img" aria-label="White line technical drawing of a threaded dental implant"></div>

    <h1 class="cover-title">Chairside<br>Roots</h1>

    <div class="tagline-row">
      <span class="tagline-rule"></span>
      <span class="tagline">start to finish</span>
      <span class="tagline-rule"></span>
    </div>

    <p class="subtitle">The Dental Helper's Field Guide</p>
    <p class="author-name">author name</p>

    <svg class="callout-lines" viewBox="0 0 421 595" aria-hidden="true" fill="none" stroke="#ffffff" stroke-width="0.8" stroke-linecap="round">
      <path d="M200 318 C215 300 240 291 265 288"/>
      <path d="M261 285 L265 288 L261 291"/>
      <path d="M229 384 C240 379 252 373 264 371"/>
      <path d="M260 368 L264 371 L261 375"/>
      <path d="M218 433 C238 437 258 434 273 429"/>
      <path d="M269 426 L273 429 L270 433"/>
      <path d="M185 511 C195 500 212 497 228 494"/>
      <path d="M224 491 L228 494 L225 498"/>
    </svg>

    <p class="callout callout--efficiency">The way to<br>Efficiency</p>
    <p class="callout callout--matters">What Matters</p>
    <p class="callout callout--takes">What It Takes</p>
    <p class="callout callout--team">Benefiting The<br>Entire TEAM</p>
  </section>
</main>
</body>
</html>
```